Business Card Design Competition

We need a business card design for our Internet Marketing company. We require both front and back designs and the final card must be 89x53mm in size, plus crop marks to 91x55mm. Colours as per logo, plus perhaps black and/or grey (#828282).
Final text must be editable (if you can supply an editable Fireworks PNG, even better)...
FRONT TEXT:
Full Name
Position
Address Line
Suburb, State, Postcode
Phone: 0000 000 000
Mobile: 0000 000 000
Email: xxx@brimleafpromo.com.au
Web: www.brimleafpromo.com.au
Rear of card should be a fresh design plus our slogan text: "Getting You Noticed" in large font, then in small text "Brimleaf Holdings Pty Ltd (ABN: 42 563 701 384)".
Target Market(s)
Small/Medium Businesses
Industry/Entity Type
Business
Look and feel
Each slider illustrates characteristics of the customer's brand and the style your logo design should communicate.

```html
<!DOCTYPE html>
<html lang="en">
<head>
<meta charset="utf-8">
<title>Brimleaf Promo – Business Card</title>
<link rel="stylesheet" href="https://fonts.googleapis.com/css2?family=Arimo:wght@400;700&display=swap">
<style>
  :root {
    --brand-orange: #f39a1e;
    --brand-green: #8cc63f;
    --band-green: #94c83d;
    --ink: #2b2b2b;
    --muted: #828282;
    --card-edge: #9a9a9a;
    --card-top: #ffffff;
    --card-shade: #f1f1f1;
    --page: #ffffff;
  }
  * { box-sizing: border-box; margin: 0; padding: 0; }
  html, body {
    width: 970px;
    height: 1200px;
    overflow: hidden;
    background: var(--page);
  }
  .canvas {
    position: relative;
    width: 970px;
    height: 1200px;
    font-family: "Arimo", Arial, sans-serif;
  }
  .card {
    position: absolute;
    left: 8px;
    width: 954px;
    border-radius: 34px;
    border: 2px solid var(--card-edge);
    overflow: hidden;
    background: linear-gradient(180deg, var(--card-shade) 0%, var(--card-top) 22%, var(--card-top) 100%);
    box-shadow: 0 2px 4px rgba(0,0,0,0.15);
  }
  .card--front { top: 8px; height: 580px; }
  .card--back  { top: 604px; height: 582px; }

  .card__band {
    position: absolute;
    left: 0; right: 0; bottom: 0;
    height: 58px;
    background: var(--band-green);
  }

  /* Front */
  .front__backdrop {
    position: absolute;
    left: 340px; top: 0;
    width: 614px; height: 520px;
    background: radial-gradient(circle at 55% 48%, rgba(140,198,63,0.16) 0%, rgba(243,154,30,0.10) 38%, rgba(255,255,255,0) 68%);
  }
  .brand {
    position: absolute;
    left: 30px; top: 128px;
    display: flex;
    align-items: center;
    gap: 30px;
  }
  .brand__dot {
    width: 318px; height: 318px;
    border-radius: 50%;
    background: var(--brand-orange);
    flex: none;
  }
  .brand__name {
    color: var(--brand-orange);
    font-weight: 400;
    font-size: 112px;
    line-height: 1.02;
    letter-spacing: 1px;
  }

  /* Back */
  .back__pattern {
    position: absolute;
    left: 0; top: 0; right: 0; bottom: 58px;
    background: linear-gradient(135deg, rgba(243,154,30,0.08) 0%, rgba(140,198,63,0.10) 50%, rgba(243,154,30,0.07) 100%);
  }
  .contact {
    position: absolute;
    left: 95px; top: 60px;
    color: var(--ink);
    font-size: 32px;
    line-height: 38px;
  }
  .contact__group + .contact__group { margin-top: 38px; }
  .contact__line { display: block; }

  .slogan {
    position: absolute;
    right: 60px; top: 70px;
    text-align: right;
    color: var(--brand-green);
    font-weight: 700;
    font-size: 46px;
    line-height: 52px;
  }
  .legal {
    position: absolute;
    right: 60px; bottom: 74px;
    text-align: right;
    color: var(--muted);
    font-size: 20px;
    line-height: 24px;
  }
</style>
</head>
<body>
<div class="canvas">

  <section class="card card--front" aria-label="Card front">
    <div class="front__backdrop" role="img" aria-label="Faint large brand symbol in soft green and orange"></div>
    <div class="brand">
      <span class="brand__dot" aria-hidden="true"></span>
      <p class="brand__name">Brimleaf<br>Promo</p>
    </div>
    <div class="card__band"></div>
  </section>

  <section class="card card--back" aria-label="Card back">
    <div class="back__pattern" role="img" aria-label="Faint repeating brand symbol pattern in pale orange and green"></div>
    <div class="contact">
      <p class="contact__group">
        <span class="contact__line">Full Name</span>
        <span class="contact__line">Position</span>
      </p>
      <p class="contact__group">
        <span class="contact__line">Address Line</span>
        <span class="contact__line">Suburb, State, Postcode</span>
      </p>
      <p class="contact__group">
        <span class="contact__line">Phone: 0000 000 000</span>
        <span class="contact__line">Mobile: 0000 000 000</span>
      </p>
      <p class="contact__group">
        <span class="contact__line">Email: xxx@brimleafpromo.com.au</span>
        <span class="contact__line">Web: www.brimleafpromo.com.au</span>
      </p>
    </div>
    <p class="slogan">Getting You<br>Noticed</p>
    <p class="legal">Brimleaf Holdings Pty Ltd (ABN: 42 563 701 384)</p>
    <div class="card__band"></div>
  </section>

</div>
</body>
</html>
```